Business Card Design needed - Something Awesome!

Need a business card designed. Company is "Harbor Vane Consulting" we do consulting and also have sales automation technology.
I'm going to use thick stock or metal, something really nice... I was thinking about a QR Code on the back that would just upload my contact info to the persons contact, etc -

This is a Strategy Company with a tech feel. I'm open to ideas but really want this to be nice!

I need a template that should include:

Name | Position or Title
D: 555.203.8146
www.harborvaneconsulting.example

I'm going to attach my contact so you can use that one, I need to get this printed.

Target Market(s)

Small to mid size customers, Entrepreneurs etc.

Industry/Entity Type

Consulting, Tech, Private Equity.

Contact Information for Business Card

Name, Phone, Maybe email, URL

Font styles to use
Sans Serif

Colors

Designer to choose only greyscale colors for use in the design.

Requirements
Must have
• Fresh, Clean, stand out from the crowd - will be on thick stock or metal.
Nice to have
• Clean, simple yet impactful.
Should not have
• Not cartoonish

```html
<!DOCTYPE html>
<html lang="en">
<head>
<meta charset="utf-8">
<title>Harbor Vane Consulting – Business Card</title>
<link rel="stylesheet" href="https://fonts.googleapis.com/css2?family=Archivo:ital,wght@0,400;0,500;0,700;1,500&display=swap">
<style>
  :root {
    --backdrop: #cfcfcf;
    --paper: #ffffff;
    --ink: #000000;
    --card-black: #050505;
    --pattern-tone: #7a7a7a;
    --soft-grey: #9c9c9c;
    --text-light: #ffffff;
  }
  * { margin: 0; padding: 0; box-sizing: border-box; }
  html, body { width: 1200px; height: 1200px; overflow: hidden; }
  body {
    background: var(--backdrop);
    font-family: "Archivo", Arial, sans-serif;
    position: relative;
  }
  .card {
    position: absolute;
    left: 162px;
    width: 876px;
    height: 513px;
    overflow: hidden;
    box-shadow: 0 2px 6px rgba(0,0,0,0.25);
  }
  .card--front { top: 66px; background: var(--paper); }
  .card--back { top: 629px; background: var(--card-black); }

  .brand-name {
    position: absolute;
    top: 150px;
    left: 0;
    width: 100%;
    text-align: center;
    font-size: 64px;
    font-weight: 500;
    letter-spacing: 4px;
    color: var(--ink);
    line-height: 1;
  }
  .pattern-band {
    position: absolute;
    top: 286px;
    left: 0;
    width: 100%;
    height: 22px;
    background: var(--pattern-tone);
  }
  .contact-panel {
    position: absolute;
    top: 309px;
    left: 0;
    width: 100%;
    height: 204px;
    background: var(--card-black);
    color: var(--text-light);
  }
  .person { position: absolute; left: 68px; top: 58px; }
  .person__name { font-size: 30px; font-weight: 700; line-height: 1.1; }
  .person__title { font-size: 24px; font-weight: 400; margin-top: 6px; }
  .contact-list {
    position: absolute;
    right: 66px;
    top: 30px;
    text-align: right;
    list-style: none;
  }
  .contact-list__cta { font-size: 24px; font-weight: 400; margin-bottom: 28px; }
  .contact-list__item {
    font-size: 21px;
    display: flex;
    justify-content: flex-end;
    align-items: center;
    gap: 12px;
    margin-bottom: 8px;
  }
  .contact-list__item svg { width: 14px; height: 14px; }

  .back-url {
    position: absolute;
    left: 82px;
    top: 422px;
    font-size: 28px;
    font-style: italic;
    font-weight: 500;
    letter-spacing: 1.5px;
    color: var(--soft-grey);
  }
</style>
</head>
<body>
  <section class="card card--front" aria-label="Business card front">
    <div class="brand-name">HARBOR VANE</div>
    <div class="pattern-band" role="img" aria-label="Decorative interlaced chain border"></div>
    <div class="contact-panel">
      <div class="person">
        <p class="person__name">Daniel R. Okafor</p>
        <p class="person__title">Founder / Owner</p>
      </div>
      <ul class="contact-list">
        <li class="contact-list__cta">Book a Meeting</li>
        <li class="contact-list__item">555.203.8146
          <svg viewBox="0 0 16 16" aria-hidden="true"><path fill="#fff" d="M3.6 1.5l2.3 2.6-1.2 1.6c.9 2 2.6 3.7 4.6 4.6l1.6-1.2 2.6 2.3-1.3 2.4C7 13.4 2.6 9 1.2 2.8z"/></svg>
        </li>
        <li class="contact-list__item">www.harborvaneconsulting.example
          <svg viewBox="0 0 16 16" aria-hidden="true"><circle cx="8" cy="8" r="7" fill="#fff"/><path d="M1 8h14M8 1c-3 3-3 11 0 14M8 1c3 3 3 11 0 14" stroke="#000" stroke-width="1.2" fill="none"/></svg>
        </li>
      </ul>
    </div>
  </section>

  <section class="card card--back" aria-label="Business card back">
    <p class="back-url">www.harborvaneconsulting.example</p>
  </section>
</body>
</html>
```